Velbrin Redesign of Website

I require my webpage to look different but this is out with my current providers platform
I will benefit from designs that use my wording (this is extremely important). I appreciate there may be a lot of wording in some areas so i would be happy with "read more" in various places. The use of my face in photo is a must and my logo is also a must which can be found on m y website www.velbrinadhd.co.uk I do not want corporate feel, i would like a warm, authentic. personal and inviting feel.

```html
<!DOCTYPE html>
<html lang="en">
<head>
<meta charset="utf-8">
<title>The Story Behind Velbrin</title>
<link href="https://fonts.googleapis.com/css2?family=Libre+Baskerville:wght@400;700&family=Dancing+Script:wght@400;500&family=Lato:wght@400;700&display=swap" rel="stylesheet">
<style>
:root{
  --teal:#1f6b66;
  --teal-dark:#164f4c;
  --teal-soft:#dcebe8;
  --mist:#eef5f4;
  --card:#fbfcfb;
  --line:#d9e6e3;
  --ink:#2b3433;
  --muted:#4a5553;
  --btn:#1e8a80;
}
*{box-sizing:border-box;margin:0;padding:0}
html,body{width:800px;height:1200px;overflow:hidden}
body{position:relative;background:linear-gradient(180deg,#ffffff 0%,#f6faf9 40%,#eef5f4 100%);font-family:"Lato",sans-serif;color:var(--ink)}
.serif{font-family:"Libre Baskerville",serif}
.script{font-family:"Dancing Script",cursive}
svg.ic{stroke:var(--teal);fill:none;stroke-width:1.6;stroke-linecap:round;stroke-linejoin:round}

/* header */
.site-header{position:absolute;left:0;top:0;width:800px;height:70px}
.brand{position:absolute;left:26px;top:18px;display:flex;align-items:center;gap:8px}
.brand-dot{width:40px;height:40px;border-radius:50%;border:1.5px solid var(--teal)}
.brand-name{font-family:"Libre Baskerville",serif;font-size:17px;font-weight:700;color:var(--teal);letter-spacing:1px}
.brand-sub{font-size:6.5px;color:var(--teal);letter-spacing:.4px;margin-top:2px;font-weight:700}
.main-nav{position:absolute;left:219px;top:30px;display:flex;gap:30px;font-size:9.5px;color:var(--ink)}
.main-nav .active{color:var(--teal);border-bottom:1.5px solid var(--teal);padding-bottom:8px}
.cta{position:absolute;left:652px;top:22px;width:89px;height:27px;border-radius:6px;background:var(--btn);color:#fff;font-size:8.5px;font-weight:700;display:flex;align-items:center;justify-content:center;gap:4px}
.fav{position:absolute;left:755px;top:22px;width:27px;height:27px;border-radius:50%;background:var(--teal-soft);display:flex;align-items:center;justify-content:center}

/* hero */
.hero-photo{position:absolute;left:380px;top:58px;width:420px;height:228px;background:linear-gradient(180deg,#dfe8ea 0%,#c9d8d9 45%,#9fb7b1 75%,#6f8f80 100%)}
.hero-title{position:absolute;left:130px;top:98px;font-size:42px;line-height:46px;color:var(--teal-dark);font-weight:700}
.hero-tag{position:absolute;left:131px;top:202px;font-size:19px;line-height:24px;color:var(--teal)}
.hero-fade{position:absolute;left:0;top:250px;width:800px;height:60px;background:linear-gradient(180deg,rgba(230,240,239,0),#e6f0ef)}

/* cards */
.card{position:absolute;background:var(--card);border:1px solid var(--line);border-radius:10px}
.intro{left:55px;top:280px;width:688px;height:160px}
.intro-icon{position:absolute;left:14px;top:22px;width:96px;height:96px;border-radius:50%;background:var(--teal-soft);display:flex;align-items:center;justify-content:center}
.intro-text{position:absolute;left:126px;top:14px;width:262px}
.intro-text h1{font-size:13px;line-height:17px;color:var(--teal-dark);font-weight:700}
.rule{width:24px;height:1.5px;background:var(--teal);margin:8px 0 9px}
.intro-text p{font-size:8.2px;line-height:12.5px;color:var(--muted);margin-bottom:8px;width:245px}
.quote{position:absolute;left:403px;top:12px;width:213px;height:138px;border:1px solid var(--line);border-radius:8px;background:#fff;text-align:center;padding-top:10px}
.quote .mark{font-family:"Libre Baskerville",serif;font-size:22px;color:var(--teal);line-height:18px}
.quote p{font-size:14px;line-height:18.5px;color:var(--teal);margin-top:6px}

.journey{left:55px;top:450px;width:332px;height:395px;padding:14px 16px}
.why{left:398px;top:450px;width:345px;height:395px;padding:14px 16px}
.card-head{display:flex;align-items:center;gap:10px;margin-bottom:12px}
.badge{width:34px;height:34px;border-radius:50%;background:var(--teal);display:flex;align-items:center;justify-content:center}
.card-head h2{font-size:13.5px;color:var(--teal-dark);font-weight:400}
.j-item{display:flex;gap:18px;padding:2px 0 8px;margin-bottom:6px;border-bottom:1px solid var(--line)}
.j-item:last-of-type{border-bottom:none}
.icirc{flex:0 0 38px;height:38px;border-radius:50%;background:var(--mist);border:1px solid var(--line);display:flex;align-items:center;justify-content:center}
.j-item p{font-size:7.9px;line-height:11.6px;color:var(--ink)}
.note{display:flex;gap:10px;align-items:center;background:var(--mist);border:1px solid var(--line);border-radius:8px;padding:8px 10px;font-size:7.9px;line-height:11.6px}
.w-item{display:flex;gap:14px;padding:4px 0 12px;margin-bottom:10px;border-bottom:1px solid var(--line)}
.w-item:last-child{border-bottom:none}
.isq{flex:0 0 46px;height:46px;border-radius:8px;background:var(--mist);display:flex;align-items:center;justify-content:center}
.w-item h3{font-family:"Libre Baskerville",serif;font-size:9.4px;line-height:13px;color:var(--teal-dark);font-weight:400;margin-bottom:4px}
.w-item p{font-size:7.9px;line-height:11.6px}

/* path */
.path-title{position:absolute;left:0;top:851px;width:800px;text-align:center;font-size:12.5px;line-height:14px;color:var(--teal-dark);z-index:2}
.path-title span{padding:0 14px;background:var(--card)}
.path{left:55px;top:858px;width:688px;height:105px;display:flex;justify-content:space-between;padding:20px 22px 0}
.step{width:76px;text-align:center;font-size:7.4px;line-height:11px;position:relative}
.step .icirc{width:38px;height:38px;margin:0 auto 6px}
.step:not(:last-child)::after{content:"";position:absolute;left:62px;top:19px;width:32px;border-top:1.5px dotted #9fb9b5}

/* approach */
.approach{left:55px;top:972px;width:688px;height:138px;display:flex;padding:12px 14px}
.appr-title{position:absolute;left:20px;top:8px;font-size:13px;color:var(--teal-dark)}
.col{flex:1;display:flex;gap:10px;padding:34px 8px 0;border-right:1px solid var(--line)}
.col:last-child{border-right:none}
.col:not(:first-child){padding-top:14px}
.col .icirc{flex:0 0 34px;height:34px}
.col h3{font-family:"Libre Baskerville",serif;font-size:8.6px;line-height:12px;color:var(--teal-dark);font-weight:400;margin-bottom:5px}
.col p{font-size:7px;line-height:11.6px}

/* footer band */
.hills{position:absolute;left:0;top:1060px;width:800px;height:140px;background:linear-gradient(180deg,rgba(207,226,223,0) 0%,#cfe2df 45%,#8fb3aa 100%);z-index:-1}
.closing-heart{position:absolute;left:208px;top:1122px;width:56px;height:56px;border-radius:50%;background:#8fbfb5;display:flex;align-items:center;justify-content:center}
.closing{position:absolute;left:270px;top:1121px;width:330px;text-align:center}
.closing .script{font-size:17px;line-height:20px;color:var(--teal)}
.closing p{font-size:8.3px;line-height:12px;margin-top:6px;color:var(--ink)}
</style>
</head>
<body>
<div class="hills" role="img" aria-label="Soft misty mountains and forest treeline"></div>

<header class="site-header">
  <div class="brand">
    <div class="brand-dot"></div>
    <div><div class="brand-name">VELBRIN</div><div class="brand-sub">ADHD COACHING &amp; WELLBEING</div></div>
  </div>
  <nav class="main-nav">
    <span class="active">Home</span><span>About Me</span><span>My Approach</span><span>Coaching</span><span>Resources</span><span>Contact</span>
  </nav>
  <div class="cta">Work With Me <svg width="9" height="9" viewBox="0 0 10 10" fill="none" stroke="#fff" stroke-width="1.5"><path d="M1 5h8M6 2l3 3-3 3"/></svg></div>
  <div class="fav"><svg class="ic" width="13" height="13" viewBox="0 0 24 24"><path d="M12 20s-8-5-8-11a4 4 0 0 1 8-1 4 4 0 0 1 8 1c0 6-8 11-8 11z"/></svg></div>
</header>

<div class="hero-photo" role="img" aria-label="Portrait of the founder, smiling in glasses, in front of a mountain lake"></div>
<div class="hero-fade"></div>
<div class="hero-title serif">The Story<br>Behind Velbrin</div>
<div class="hero-tag script">Helping others began<br>with understanding myself.</div>

<section class="card intro">
  <div class="intro-icon"><svg class="ic" width="54" height="54" viewBox="0 0 48 48"><circle cx="24" cy="13" r="7"/><path d="M10 42c0-10 6-16 14-16s14 6 14 16"/><path d="M24 40s-6-3.5-6-7.5a3 3 0 0 1 6-.8 3 3 0 0 1 6 .8c0 4-6 7.5-6 7.5z"/></svg></div>
  <div class="intro-text">
    <h1 class="serif">My name is Rhona Kessel Dunn,<br>founder of Velbrin.</h1>
    <div class="rule"></div>
    <p>I am an ADHD coach and wellbeing practitioner with lived experience of ADHD and autism (AuDHD).</p>
    <p>I combine professional expertise with real-life experience to offer compassionate, practical support that helps you better understand yourself, your brain and your wellbeing.</p>
  </div>
  <div class="quote">
    <div class="mark">&ldquo;</div>
    <p class="script">You don't need to have<br>everything figured out<br>before reaching out.<br>We'll take things one<br>step at a time. Together.</p>
  </div>
</section>

<section class="card journey">
  <div class="card-head"><div class="badge"><svg width="16" height="16" viewBox="0 0 24 24" fill="none" stroke="#fff" stroke-width="1.8"><path d="M12 20s-8-5-8-11a4 4 0 0 1 8-1 4 4 0 0 1 8 1c0 6-8 11-8 11z"/></svg></div><h2 class="serif">My Journey</h2></div>
  <div class="j-item"><div class="icirc"><svg class="ic" width="18" height="18" viewBox="0 0 24 24"><path d="M12 21V9M12 14c-4 0-6-3-6-6 4 0 6 2 6 6zM12 12c0-4 2-6 6-6 0 3-2 6-6 6"/></svg></div>
    <p>My adult ADHD diagnosis came during a period of profound self-discovery following a mental health breakdown. For many years, my ADHD went unrecognised and was treated with antidepressants, which never addressed the underlying causes of my struggles.</p></div>
  <div class="j-item"><div class="icirc"><svg class="ic" width="20" height="20" viewBox="0 0 24 24"><path d="M12 12c-2-3-4-4-6-4a4 4 0 0 0 0 8c2 0 4-1 6-4zm0 0c2 3 4 4 6 4a4 4 0 0 0 0-8c-2 0-4 1-6 4z"/></svg></div>
    <p>As my understanding grew, I recognised I am also autistic – something that is common alongside ADHD. Around 30–70% of autistic people also have ADHD, and many adults only receive the second neurotype once the first has been correctly identified. This changed everything.</p></div>
  <div class="j-item"><div class="icirc"><svg class="ic" width="18" height="18" viewBox="0 0 24 24"><path d="M12 12s-4-2.5-4-5a2 2 0 0 1 4-.5 2 2 0 0 1 4 .5c0 2.5-4 5-4 5zM3 14l4 5h5M21 14l-4 5h-5"/></svg></div>
    <p>These experiences strengthened my passion for helping neurodivergent individuals better understand their brains, develop self-compassion and find strategies that work. I believe every brain deserves understanding, support and practical tools for wellbeing.</p></div>
  <div class="j-item"><div class="icirc"><svg class="ic" width="18" height="18" viewBox="0 0 24 24"><path d="M2 9l10-5 10 5-10 5zM6 11v5c3 2 9 2 12 0v-5"/></svg></div>
    <p>This personal journey inspired me to deepen my professional knowledge and training. I qualified as an Integrative Counsellor (HNC) and then as a Health &amp; Wellbeing Coach through Clearfield Learning Academy (QHS-recognised), followed by specialist training in Autism, ADHD and Somatic Coaching.</p></div>
  <div class="note"><svg class="ic" width="22" height="22" viewBox="0 0 24 24"><path d="M4 20C8 14 12 10 20 4M9 15c-2-3 0-6 3-6M14 10c3-1 5 1 5 3"/></svg><span>I believe learning never stops, and I continue to develop my knowledge in neurodiversity, wellbeing and mental health so I can offer the best possible support.</span></div>
</section>

<section class="card why">
  <div class="card-head"><div class="badge"><svg width="16" height="16" viewBox="0 0 24 24" fill="none" stroke="#fff" stroke-width="1.8"><path d="M12 20s-8-5-8-11a4 4 0 0 1 8-1 4 4 0 0 1 8 1c0 6-8 11-8 11z"/></svg></div><h2 class="serif">Why Velbrin Was Created</h2></div>
  <div class="w-item"><div class="isq"><svg class="ic" width="22" height="22" viewBox="0 0 24 24"><path d="M12 18v-8M12 11c-3 0-5-2-5-5 3 0 5 2 5 5zM12 11c0-3 2-5 5-5 0 3-2 5-5 5M5 18h14"/></svg></div>
    <div><h3>I wanted to offer the kind of support I wish I had when I was struggling.</h3><p>A safe, welcoming space where neurodivergent people feel seen, understood and supported to thrive in their own way.</p></div></div>
  <div class="w-item"><div class="isq"><svg class="ic" width="22" height="22" viewBox="0 0 24 24"><rect x="3" y="7" width="18" height="13" rx="2"/><path d="M9 7V5h6v2M3 12h18M10 12v2h4v-2"/></svg></div>
    <div><h3>I believe in practical, lasting support.</h3><p>I empower people with knowledge, strategies and tools they can continue using long after our work together has ended.</p></div></div>
  <div class="w-item"><div class="isq"><svg class="ic" width="24" height="24" viewBox="0 0 24 24"><circle cx="6" cy="8" r="2"/><circle cx="18" cy="8" r="2"/><circle cx="12" cy="11" r="1.6"/><path d="M3 20v-6l3-2 3 2v6M15 20v-6l3-2 3 2v6M10 20v-4l2-2 2 2v4M12 5s-2-1.2-2-2.4a1 1 0 0 1 2-.2 1 1 0 0 1 2 .2C14 3.8 12 5 12 5z"/></svg></div>
    <div><h3>I understand the reality of neurodivergent family life.</h3><p>As a mother to three neurodivergent children, I have invaluable lived experience of advocacy, navigating systems and carving a calmer home life.</p></div></div>
  <div class="w-item"><div class="isq"><svg class="ic" width="24" height="24" viewBox="0 0 24 24"><path d="M12 20s-8-5-8-11a4 4 0 0 1 8-1 4 4 0 0 1 8 1c0 6-8 11-8 11z"/></svg></div>
    <div><h3>My personal experiences and professional qualifications shape the compassionate, neuro-affirming approach at the heart of everything I do.</h3></div></div>
</section>

<section class="card path">
  <div class="step"><div class="icirc"><svg class="ic" width="18" height="18" viewBox="0 0 24 24"><path d="M3 11l9-7 9 7M5 10v10h14V10M10 20v-6h4v6"/></svg></div>Housing<br>Officer</div>
  <div class="step"><div class="icirc"><svg class="ic" width="18" height="18" viewBox="0 0 24 24"><path d="M12 5a4 4 0 0 0-7 3 4 4 0 0 0 1 7 4 4 0 0 0 6 3zM12 5a4 4 0 0 1 7 3 4 4 0 0 1-1 7 4 4 0 0 1-6 3zM12 5v15"/></svg></div>Mental Health<br>Breakdown</div>
  <div class="step"><div class="icirc"><svg class="ic" width="18" height="18" viewBox="0 0 24 24"><circle cx="12" cy="9" r="6"/><path d="M12 21v-9M9 12l3 2 3-3"/></svg></div>ADHD<br>Diagnosis</div>
  <div class="step"><div class="icirc"><svg class="ic" width="20" height="20" viewBox="0 0 24 24"><path d="M12 12c-2-3-4-4-6-4a4 4 0 0 0 0 8c2 0 4-1 6-4zm0 0c2 3 4 4 6 4a4 4 0 0 0 0-8c-2 0-4 1-6 4z"/></svg></div>Understanding<br>Autism (AuDHD)</div>
  <div class="step"><div class="icirc"><svg class="ic" width="18" height="18" viewBox="0 0 24 24"><path d="M3 5h6a3 3 0 0 1 3 3v12a2 2 0 0 0-2-2H3zM21 5h-6a3 3 0 0 0-3 3v12a2 2 0 0 1 2-2h7z"/></svg></div>Integrative<br>Counselling<br>Study</div>
  <div class="step"><div class="icirc"><svg class="ic" width="18" height="18" viewBox="0 0 24 24"><path d="M2 9l10-5 10 5-10 5zM6 11v5c3 2 9 2 12 0v-5"/></svg></div>Health &amp;<br>Wellbeing Coach<br>(QHS-recognised)</div>
  <div class="step"><div class="icirc"><svg class="ic" width="18" height="18" viewBox="0 0 24 24"><path d="M9 17h6M10 20h4M12 3a6 6 0 0 0-4 10c1 1 1 2 1 3h6c0-1 0-2 1-3a6 6 0 0 0-4-10z"/></svg></div>Specialist Training in<br>Autism, ADHD &amp;<br>Somatic Coaching</div>
  <div class="step"><div class="icirc"><svg class="ic" width="20" height="20" viewBox="0 0 24 24"><path d="M2 19l7-12 4 6 3-4 6 10z"/></svg></div>Velbrin<br>Created</div>
</section>
<div class="path-title serif"><span>My Path</span></div>

<section class="card approach">
  <div class="appr-title serif">The Velbrin Approach</div>
  <div class="col"><div class="icirc"><svg class="ic" width="17" height="17" viewBox="0 0 24 24"><path d="M3 11l9-7 9 7M5 10v10h14V10M10 20v-6h4v6"/></svg></div>
    <div><h3>Lived &amp; Tested</h3><p>Many strategies and tools come from my own family's journey. They are real, tested and proven to make a difference in real life.</p></div></div>
  <div class="col"><div class="icirc"><svg class="ic" width="18" height="18" viewBox="0 0 24 24"><path d="M12 12c-2-3-4-4-6-4a4 4 0 0 0 0 8c2 0 4-1 6-4zm0 0c2 3 4 4 6 4a4 4 0 0 0 0-8c-2 0-4 1-6 4z"/></svg></div>
    <div><h3>Individual, Not<br>One-Size-Fits-All</h3><p>Every neurodivergent person is unique. There is no single strategy or approach that works for everyone. I work alongside you to find what works for you.</p></div></div>
  <div class="col"><div class="icirc"><svg class="ic" width="17" height="17" viewBox="0 0 24 24"><path d="M5 19C5 10 10 5 19 5c0 9-5 14-14 14zM5 19l8-8"/></svg></div>
    <div><h3>Practical &amp;<br>Sustainable</h3><p>I focus on realistic, practical approaches that fit into your everyday life and support your wellbeing in a way that feels manageable and meaningful.</p></div></div>
  <div class="col"><div class="icirc"><svg class="ic" width="17" height="17" viewBox="0 0 24 24"><path d="M12 20s-8-5-8-11a4 4 0 0 1 8-1 4 4 0 0 1 8 1c0 6-8 11-8 11z"/></svg></div>
    <div><h3>Compassionate &amp;<br>Neuro-Affirming</h3><p>I believe neurodivergent people deserve support that is centred around the individual – not around trying to fit into a world that wasn't designed with neurodivergent minds in mind.</p></div></div>
</section>

<div class="closing-heart"><svg width="28" height="28" viewBox="0 0 24 24" fill="none" stroke="#fff" stroke-width="1.6"><path d="M12 20s-8-5-8-11a4 4 0 0 1 8-1 4 4 0 0 1 8 1c0 6-8 11-8 11z"/></svg></div>
<div class="closing">
  <div class="script">Because sometimes the smallest changes<br>can make the biggest difference.</div>
  <p>Whether you are taking a brave step forward or just here to explore,<br>you are part of a journey—one that begins with understanding.</p>
</div>
</body>
</html>
```